Property developer, money partner needs business card design using logo concept provided

Our company develops residential properties, does money lends for joint ventures in property deals and finds property deals for other money partners. We have provided a basic logo for you to work from. Any graphic or logo design on the card is to communicate development and finance collaboration. Color choice is not so important for us, but color choice does need to reflect professionalism.

```html
<!DOCTYPE html>
<html lang="en">
<head>
<meta charset="utf-8">
<title>Keystone Yard – Business Card</title>
<link rel="stylesheet" href="https://fonts.googleapis.com/css2?family=Open+Sans:wght@400;600;700&display=swap">
<style>
  :root {
    --stage: #3b3b3b;
    --card: #151515;
    --blue: #1a73c9;
    --blue-bright: #1e88e5;
    --red: #b3262b;
    --white: #f2f2f2;
    --muted: #d8d8d8;
  }
  * { box-sizing: border-box; margin: 0; padding: 0; }
  html, body {
    width: 1200px; height: 801px; overflow: hidden;
    background: var(--stage);
    font-family: "Open Sans", Arial, sans-serif;
  }
  .stage {
    width: 1200px; height: 801px;
    display: flex; align-items: center; justify-content: center; gap: 44px;
  }
  .card {
    position: relative;
    width: 540px; height: 310px;
    background: var(--card);
    border-bottom: 3px solid var(--blue);
    box-shadow: 0 14px 30px rgba(0,0,0,.45);
    overflow: hidden;
  }

  /* Front */
  .brand-mark {
    position: absolute; right: 34px; top: 40px;
    display: flex; align-items: center; gap: 10px;
  }
  .brand-mark .dot {
    width: 44px; height: 44px; border-radius: 50%;
    background: var(--blue);
  }
  .brand-mark .name {
    color: var(--white); font-weight: 700; font-size: 15px; letter-spacing: 3px;
  }
  .divider {
    position: absolute; left: 34px; right: 34px; top: 176px;
    height: 1px; background: var(--blue);
  }
  .person { position: absolute; left: 34px; top: 116px; }
  .person .full-name {
    color: var(--blue-bright); font-weight: 700; font-size: 22px; letter-spacing: .5px;
  }
  .person .role { color: var(--white); font-size: 14px; margin-top: 2px; }
  .contacts { position: absolute; left: 34px; top: 192px; list-style: none; }
  .contacts li {
    display: flex; align-items: center; gap: 9px;
    color: var(--white); font-size: 14px; line-height: 24px;
  }
  .contacts svg { width: 12px; height: 12px; fill: var(--red); flex: none; }
  .address {
    position: absolute; right: 34px; top: 192px; text-align: right;
    color: var(--white); font-size: 14px; line-height: 22px;
  }

  /* Back */
  .back-brand { position: absolute; left: 34px; bottom: 40px; }
  .back-brand .name {
    color: var(--white); font-weight: 700; font-size: 32px; letter-spacing: 6px; line-height: 1.1;
  }
  .back-brand .tagline {
    color: var(--white); font-weight: 700; font-size: 20px; letter-spacing: 4px;
  }
  .back-brand .acn {
    color: var(--muted); font-size: 13px; letter-spacing: 3px; margin-top: 4px; padding-left: 40px;
  }
</style>
</head>
<body>
<main class="stage">
  <section class="card card-front" aria-label="Business card front">
    <div class="brand-mark">
      <span class="dot"></span>
      <span class="name">KEYSTONE YARD</span>
    </div>
    <div class="person">
      <p class="full-name">DAN CORLEY</p>
      <p class="role">President</p>
    </div>
    <div class="divider"></div>
    <ul class="contacts">
      <li>
        <svg viewBox="0 0 24 24" aria-hidden="true"><path d="M6.6 10.8a15.1 15.1 0 0 0 6.6 6.6l2.2-2.2a1 1 0 0 1 1-.25 11.4 11.4 0 0 0 3.6.57 1 1 0 0 1 1 1V20a1 1 0 0 1-1 1A17 17 0 0 1 3 4a1 1 0 0 1 1-1h3.5a1 1 0 0 1 1 1c0 1.25.2 2.45.57 3.57a1 1 0 0 1-.25 1z"/></svg>
        555-014-2287
      </li>
      <li>
        <svg viewBox="0 0 24 24" aria-hidden="true"><path d="M2 5h20v14H2zm2 2v.5l8 5 8-5V7l-8 5z"/></svg>
        dcorley@keystoneyard.com
      </li>
      <li>
        <svg viewBox="0 0 24 24" aria-hidden="true"><path d="M12 2a10 10 0 1 0 0 20 10 10 0 0 0 0-20zm6.9 9h-3a15 15 0 0 0-1.3-5.6A8 8 0 0 1 18.9 11zM12 4.1c.9 1.3 1.7 3.6 1.9 6.9h-3.8c.2-3.3 1-5.6 1.9-6.9zM4.1 13h3a15 15 0 0 0 1.3 5.6A8 8 0 0 1 4.1 13zm3-2h-3a8 8 0 0 1 4.3-5.6A15 15 0 0 0 7.1 11zM12 19.9c-.9-1.3-1.7-3.6-1.9-6.9h3.8c-.2 3.3-1 5.6-1.9 6.9zm2.6-1.3a15 15 0 0 0 1.3-5.6h3a8 8 0 0 1-4.3 5.6z"/></svg>
        www.keystoneyard.com
      </li>
    </ul>
    <address class="address">
      1180 Harbor Crest Way<br>
      Seaview CA 90210
    </address>
  </section>

  <section class="card card-back" aria-label="Business card back">
    <div class="back-brand">
      <p class="name">KEYSTONE YARD</p>
      <p class="tagline">Property Solutions</p>
      <p class="acn">A.C.N 104 228 316</p>
    </div>
  </section>
</main>
</body>
</html>
```